Stylish business cards for KX7

To create an appealing and professional business card design for a WOMEN Owned Construction Supply Company.
2 sided card. Incorporate brand elements, curvy, colorful, sleek and bright. No solid white background. attached samples of styles added shapes/ribbons. Want something with that WOW that looks awesome, factor. It is a new logo, so feel free to mess with logo colors in the blue and teal factors that can look good with both dark and light background. If you want to try a watermark with just the KX7, without the "Supply" that might look cool to.

Industry/Entity Type

Women owned construction supply company

Contact Information for Business Card

Name, Title, and phone number and email, web page. maybe spot for qr code.

Font styles to use
Sans Serif

Requirements
Nice to have
• would love to see colors, maybe stylish ribbon dividers or some sort of 2 or 3 tone color card that compliments logo.
Should not have
• Please do not have all white background. Do not include Home/reale state/ or building images.

```html
<!DOCTYPE html>
<html lang="en">
<head>
<meta charset="utf-8">
<title>KX7 Supply – Business Cards</title>
<link rel="stylesheet" href="https://fonts.googleapis.com/css2?family=Montserrat:wght@400;500;700&display=swap">
<style>
  :root {
    --stage: #1d1d1f;
    --navy: #1b3657;
    --teal: #2596be;
    --paper: #f4f4f4;
    --white: #ffffff;
  }
  * { box-sizing: border-box; margin: 0; padding: 0; }
  html, body { width: 1200px; height: 1059px; overflow: hidden; }
  body {
    position: relative;
    background: var(--stage);
    font-family: "Montserrat", sans-serif;
  }
  .card {
    position: absolute;
    background: var(--navy);
    border-radius: 18px;
    overflow: hidden;
  }
  .card-front { left: 257px; top: 89px; width: 687px; height: 390px; }
  .card-back  { left: 254px; top: 547px; width: 693px; height: 393px; }

  .front-shape { position: absolute; inset: 0; width: 100%; height: 100%; }

  .name-marker {
    position: absolute; left: 0; top: 47px;
    width: 15px; height: 36px; background: var(--teal);
  }
  .person { position: absolute; left: 32px; top: 43px; }
  .person-name {
    color: var(--teal); font-weight: 700; font-size: 22px;
    letter-spacing: 0.3px; line-height: 1.1;
  }
  .person-title {
    color: var(--white); font-weight: 400; font-size: 15px; margin-top: 3px;
  }
  .address {
    position: absolute; left: 32px; top: 209px;
    color: var(--white); font-size: 15px; line-height: 22px;
  }
  .contacts {
    position: absolute; left: 32px; top: 271px; list-style: none;
  }
  .contacts li {
    display: flex; align-items: center; gap: 7px;
    color: var(--white); font-size: 15px; height: 28px;
  }
  .contacts svg { width: 12px; height: 12px; fill: var(--teal); flex: none; }

  .brand-name {
    position: absolute; font-weight: 700; white-space: nowrap;
    transform: translate(-50%, -50%);
  }
  .card-front .brand-name { left: 525px; top: 199px; font-size: 36px; color: var(--navy); }
  .card-back .brand-name  { left: 346px; top: 196px; font-size: 44px; color: var(--white); }
</style>
</head>
<body>
  <section class="card card-front" aria-label="Card front">
    <svg class="front-shape" viewBox="0 0 687 390" preserveAspectRatio="none" aria-hidden="true">
      <path d="M413,0 L443,0 C355,70 330,250 460,390 L445,390 C310,260 320,80 413,0 Z" fill="var(--teal)"/>
      <path d="M452,0 L687,0 L687,390 L475,390 C345,255 360,75 452,0 Z" fill="var(--paper)"/>
    </svg>

    <div class="name-marker"></div>
    <div class="person">
      <p class="person-name">DANA HOLLIS</p>
      <p class="person-title">CEO/Founder</p>
    </div>

    <p class="address">P.O Box 4210 Harbor Road<br>Westfield AB 10101</p>

    <ul class="contacts">
      <li>
        <svg viewBox="0 0 24 24"><path d="M6.6 10.8a15.1 15.1 0 0 0 6.6 6.6l2.2-2.2c.3-.3.7-.4 1-.2 1.1.4 2.3.6 3.6.6.6 0 1 .4 1 1V20c0 .6-.4 1-1 1A17 17 0 0 1 3 4c0-.6.4-1 1-1h3.5c.6 0 1 .4 1 1 0 1.3.2 2.5.6 3.6.1.3 0 .7-.2 1z"/></svg>
        555.310.4827
      </li>
      <li>
        <svg viewBox="0 0 24 24"><path d="M2 5h20v14H2z M2 5l10 8 10-8" /></svg>
        info@kx7supply.com.au
      </li>
      <li>
        <svg viewBox="0 0 24 24"><path d="M12 2a10 10 0 1 0 0 20 10 10 0 0 0 0-20zm7.9 9h-3.5a15 15 0 0 0-1.4-6.2A8 8 0 0 1 19.9 11zM12 4c1 1.3 2.2 3.8 2.4 7H9.6C9.8 7.8 11 5.3 12 4zM9 4.8A15 15 0 0 0 7.6 11H4.1A8 8 0 0 1 9 4.8zM4.1 13h3.5A15 15 0 0 0 9 19.2 8 8 0 0 1 4.1 13zM12 20c-1-1.3-2.2-3.8-2.4-7h4.8c-.2 3.2-1.4 5.7-2.4 7zm3 -.8a15 15 0 0 0 1.4-6.2h3.5a8 8 0 0 1-4.9 6.2z"/></svg>
        www.kx7supply.com.au
      </li>
    </ul>

    <p class="brand-name">KX7 Supply</p>
  </section>

  <section class="card card-back" aria-label="Card back">
    <p class="brand-name">KX7 Supply</p>
  </section>
</body>
</html>
```